Vantor 7 Skins

Hey I need 2 stickers made one for my vantor 7 Rower and one for my vantor 7 dyn arc.I have attached some images of the rower and dyn arc as well as some photos of the rower and ski with some stickers already done.And i have attached my logo so you can get a feel for how i would like it designed and the logos that need to be included.

Target Market(s)

TO BE STUCK ON THE MACHINES IN A GYM

The rowers will need to be reversable.

Font styles to use
Serif
Sans Serif
Other font styles liked:
• LATO

Colors
0392cd
33a6d7
85cae6
ffffff
0255a3
3176b5
cedeed
85acd3
e34197

```html
<!DOCTYPE html>
<html lang="en">
<head>
<meta charset="utf-8">
<title>Korvale – Machine Sticker Strips</title>
<link href="https://fonts.googleapis.com/css2?family=Lato:wght@700&display=swap" rel="stylesheet">
<style>
  :root {
    --board: #1e1e1e;
    --navy-deep: #05062a;
    --navy: #0a0f4a;
    --royal: #0255a3;
    --azure: #0392cd;
    --violet: #3a2f8a;
    --coral: #b0607a;
    --blue-right: #0a2a8a;
    --white: #ffffff;
  }
  * { margin: 0; padding: 0; box-sizing: border-box; }
  html, body {
    width: 1200px;
    height: 680px;
    overflow: hidden;
    background: var(--board);
  }
  .artboard {
    position: relative;
    width: 1200px;
    height: 680px;
    background: var(--board);
    font-family: "Lato", sans-serif;
  }
  .sticker {
    position: absolute;
    left: 36px;
    height: 140px;
    overflow: hidden;
  }
  .sticker--rower { top: 161px; width: 1141px; }
  .sticker--dyn-arc { top: 338px; width: 1138px; }

  .sticker__art {
    position: absolute;
    inset: 0;
  }
  .sticker--rower .sticker__art {
    background: linear-gradient(90deg, var(--royal) 0%, var(--azure) 25%, var(--royal) 50%, var(--navy) 75%, var(--navy-deep) 100%);
  }
  .sticker--dyn-arc .sticker__art {
    background: linear-gradient(90deg, var(--navy-deep) 0%, var(--navy) 30%, var(--violet) 50%, var(--coral) 58%, var(--royal) 75%, var(--blue-right) 100%);
  }

  .brand {
    position: absolute;
    text-align: center;
    color: var(--white);
    transform: translateX(-50%);
    white-space: nowrap;
  }
  .sticker--rower .brand { left: 922px; top: 30px; }
  .sticker--dyn-arc .brand { left: 936px; top: 28px; }
  .brand__name {
    display: block;
    font-size: 62px;
    font-weight: 700;
    line-height: 1;
    letter-spacing: 3px;
  }
  .brand__tagline {
    display: block;
    margin-top: 10px;
    font-size: 20px;
    font-weight: 700;
    line-height: 1;
  }
</style>
</head>
<body>
<main class="artboard">
  <section class="sticker sticker--rower">
    <div class="sticker__art" role="img" aria-label="Abstract speed-light artwork in cyan, blue and magenta on dark navy"></div>
    <div class="brand">
      <span class="brand__name">KORVALE</span>
      <span class="brand__tagline">PERSONAL &amp; GROUP</span>
    </div>
  </section>

  <section class="sticker sticker--dyn-arc">
    <div class="sticker__art" role="img" aria-label="Abstract diagonal light artwork in violet, coral and blue on dark navy"></div>
    <div class="brand">
      <span class="brand__name">KORVALE</span>
      <span class="brand__tagline">PERSONAL &amp; GROUP</span>
    </div>
  </section>
</main>
</body>
</html>
```